Lanternway 7.5 - Educational Guide/Course-pack/Worksheet

Our Lanternway 7.5 toolkit is an educational workshop that focuses on inspiring student initiatives in the classroom! We need a new educational course guide or course-pack for students/teachers that clearly outlines or explains the program steps, offers helpful tips and includes empty spaces/lines where their can write down their great ideas or notes. This will include a;

- Teachers Guide (1 Page)
- Student Guide/Worksheet (4 Pages)
- Group Pack Resources (3 Pages)

This will consist of designing/formatting text, stock animation/icons, font, etc. We have included our new logo (color, branding, etc.) and all of the text for each separate course-pack. We have also attached our new website to give you an idea of the program style.

Our workshop can be for any school project like Technology, Community, Environment, Art, Science, etc.

Target Market(s)

High School Students/Teachers

Industry/Entity Type

Education

Font styles to use
Sans Serif

Colors
f68e4e
acd037
34a7d8

Requirements
Must have
• Use our brand colors from logo.
Should not have
• Should not be too childish.

```html
<!DOCTYPE html>
<html lang="en">
<head>
<meta charset="utf-8">
<title>The Big Pitch – Worksheet</title>
<link href="https://fonts.googleapis.com/css2?family=Roboto+Condensed:wght@300;400;700&display=swap" rel="stylesheet">
<style>
  :root {
    --ink: #111111;
    --paper: #ffffff;
    --frame: #222222;
    --brand-orange: #f68e4e;
    --brand-green: #acd037;
    --brand-blue: #34a7d8;
    --art-tone-a: #c9e6f3;
    --art-tone-b: #34a7d8;
  }
  html, body {
    margin: 0;
    padding: 0;
    overflow: hidden;
    background: var(--paper);
  }
  .sheet {
    position: relative;
    width: 928px;
    height: 1200px;
    box-sizing: border-box;
    border: 1px solid var(--frame);
    background: var(--paper);
    color: var(--ink);
    font-family: "Roboto Condensed", "Arial Narrow", sans-serif;
    font-weight: 300;
    overflow: hidden;
  }
  .step-title {
    position: absolute;
    left: 43px;
    top: 36px;
    margin: 0;
    font-size: 24px;
    font-weight: 700;
    letter-spacing: 0.2px;
  }
  .step-number { color: var(--brand-orange); }
  .section-title {
    position: absolute;
    left: 239px;
    margin: 0;
    font-size: 21px;
    font-weight: 700;
    color: var(--brand-blue);
  }
  .section-title.prepare { top: 41px; }
  .section-title.present { top: 303px; }
  .copy {
    position: absolute;
    left: 239px;
    margin: 0;
    font-size: 17.1px;
    line-height: 22px;
    white-space: nowrap;
  }
  .copy.prepare-intro { top: 65px; }
  .copy.present-intro { top: 349px; }
  .copy.closing { top: 944px; }
  .column-label {
    position: absolute;
    top: 112px;
    margin: 0;
    font-size: 17px;
  }
  .column-label.positive { left: 239px; }
  .column-label.challenges { left: 511px; }
  .write-line {
    position: absolute;
    height: 0;
    border-top: 1.6px solid var(--ink);
  }
  .write-line.col-left { left: 239px; width: 233px; }
  .write-line.col-right { left: 511px; width: 232px; }
  .write-line.full { left: 239px; width: 504px; }
  .prompt {
    position: absolute;
    left: 241px;
    margin: 0;
    font-size: 17px;
    line-height: 22px;
    white-space: nowrap;
  }
  .prompt::before {
    content: "";
    display: inline-block;
    width: 6px;
    height: 6px;
    border-radius: 50%;
    background: var(--brand-green);
    margin-right: 8px;
    vertical-align: middle;
    position: relative;
    top: -2px;
  }
  .presenter-art {
    position: absolute;
    left: 73px;
    top: 163px;
    width: 130px;
    height: 106px;
    border-radius: 4px;
    background: linear-gradient(135deg, var(--art-tone-a), var(--art-tone-b));
  }
</style>
</head>
<body>
<main class="sheet">
  <h1 class="step-title"><span class="step-number">4.</span>&nbsp; The Big Pitch</h1>

  <div class="presenter-art" role="img" aria-label="Illustration of a presenter pointing at a pie chart on a board"></div>

  <h2 class="section-title prepare">Prepare</h2>
  <p class="copy prepare-intro">List all the positive points and all the challenges you may have in doing this project.</p>

  <p class="column-label positive">Positive Points</p>
  <p class="column-label challenges">Challenges</p>

  <div class="write-line col-left" style="top:162px"></div>
  <div class="write-line col-left" style="top:194px"></div>
  <div class="write-line col-left" style="top:226px"></div>
  <div class="write-line col-left" style="top:255px"></div>
  <div class="write-line col-left" style="top:284px"></div>

  <div class="write-line col-right" style="top:162px"></div>
  <div class="write-line col-right" style="top:194px"></div>
  <div class="write-line col-right" style="top:226px"></div>
  <div class="write-line col-right" style="top:255px"></div>
  <div class="write-line col-right" style="top:284px"></div>

  <h2 class="section-title present">Present</h2>
  <p class="copy present-intro">Two or more members of your team will present your project to the other groups.<br>
  Your presentation should answer these questions in an interesting, fun, or original way!<br>
  If you have time, make a poster with a visual of your slogan, logo, or ad.</p>

  <p class="prompt" style="top:454px">Where did your idea come from?</p>
  <div class="write-line full" style="top:509px"></div>
  <div class="write-line full" style="top:539px"></div>

  <p class="prompt" style="top:575px">What is the idea and what will have to be done?</p>
  <div class="write-line full" style="top:632px"></div>
  <div class="write-line full" style="top:661px"></div>

  <p class="prompt" style="top:690px">Why is this a good idea?</p>
  <div class="write-line full" style="top:747px"></div>
  <div class="write-line full" style="top:776px"></div>

  <p class="prompt" style="top:817px">Who will benefit from your project?</p>
  <div class="write-line full" style="top:873px"></div>
  <div class="write-line full" style="top:903px"></div>

  <p class="copy closing">All the other teams will look for missing details, ask questions, find problems, and<br>
  offer suggestions!&nbsp; So be ready to defend your idea!</p>
</main>
</body>
</html>
```